QKT (Guaranteed Project)

**Note: The girl image is not mandatory, that was just an idea, it may even look better with just text and no girl

TEXT (Marlon Pikeway and Brevix logos large please):

EVERYONE STAND TALL (the font from the image below for everyone stand tall looks good, kind of retro)

QKT WEEKEND 2014
SUNDAY MAY 25

430-9pm

QKT after party starts at 9pm-2am

Featuring
MARLON PIKEWAY (SF) (use logo, largest name)
BREVIX (Sac) (use logo w/out the text below it, and slightly smaller than marlon pikeway)

at Z!P Uptown 3871 J Street 21+

Reason: The mgr wants to review them and hasn't said yes yet.

Target Market(s)

House/Electronic Music Night Club

Font styles to use
Sans Serif

Colors
ec2027
ffffff

Requirements
Nice to have
• Would look nice with the red background and maybe a reddish filter on the girl

```html
<!DOCTYPE html>
<html lang="en">
<head>
<meta charset="utf-8">
<title>Everyone Stand Tall – QKT Weekend 2014</title>
<link rel="stylesheet" href="https://fonts.googleapis.com/css2?family=Anton&display=swap">
<style>
  :root {
    --red: #ec2027;
    --red-light: #f06a6e;
    --red-soft: #e8474e;
    --white: #ffffff;
  }
  html, body {
    margin: 0;
    padding: 0;
    width: 939px;
    height: 1200px;
    overflow: hidden;
    background: var(--red);
  }
  .poster {
    display: block;
    width: 939px;
    height: 1200px;
  }
  .poster text {
    font-family: "Anton", "Impact", sans-serif;
    fill: var(--white);
  }
  .logo-ring {
    fill: none;
    stroke: var(--white);
    stroke-width: 3;
  }
</style>
</head>
<body>
<svg class="poster" viewBox="0 0 939 1200" xmlns="http://www.w3.org/2000/svg">
  <defs>
    <linearGradient id="photoTone" x1="0" y1="0" x2="1" y2="1">
      <stop offset="0" stop-color="var(--red-soft)"/>
      <stop offset="0.55" stop-color="var(--red-light)"/>
      <stop offset="1" stop-color="var(--red)"/>
    </linearGradient>
  </defs>

  <rect class="photo-backdrop" x="0" y="0" width="939" height="1200" fill="url(#photoTone)"
        role="img" aria-label="Red-filtered close-up photo of a woman with a finger at her lips"/>

  <g class="headline">
    <text x="52" y="232" font-size="185" textLength="660" lengthAdjust="spacingAndGlyphs">EVERYONE</text>
    <text x="723" y="110" font-size="43" textLength="138" lengthAdjust="spacingAndGlyphs">STAND</text>
    <text x="52" y="418" font-size="184" textLength="511" lengthAdjust="spacingAndGlyphs">TALL</text>
  </g>

  <g class="event-date">
    <text x="52" y="535" font-size="59" textLength="198" lengthAdjust="spacingAndGlyphs">SUNDAY</text>
    <text x="52" y="623" font-size="96" textLength="206" lengthAdjust="spacingAndGlyphs">MAY</text>
    <text x="282" y="623" font-size="139" textLength="184" lengthAdjust="spacingAndGlyphs">25</text>
  </g>

  <g class="event-time">
    <text x="52" y="712" font-size="68" textLength="230" lengthAdjust="spacingAndGlyphs">430-9pm</text>
    <text x="52" y="773" font-size="23" textLength="331" lengthAdjust="spacingAndGlyphs">QKT after party starts at 9pm-2am</text>
  </g>

  <g class="event-details">
    <text x="52" y="884" font-size="96" textLength="821" lengthAdjust="spacingAndGlyphs">QKT WEEKEND 2014</text>
    <text x="34" y="962" font-size="70" textLength="839" lengthAdjust="spacingAndGlyphs">HOUSE MUSIC AT ITS FINEST</text>
    <text x="34" y="1038" font-size="70" textLength="639" lengthAdjust="spacingAndGlyphs">Z!P Uptown 3871 J Street 21+</text>
  </g>

  <g class="sponsor-logos">
    <circle class="logo-ring" cx="66" cy="1120" r="28"/>
    <text x="110" y="1150" font-size="74" textLength="380" lengthAdjust="spacingAndGlyphs">MARLON PIKEWAY</text>
    <text x="510" y="1150" font-size="22" textLength="110" lengthAdjust="spacingAndGlyphs">HALDEN MUSIC</text>
    <text x="640" y="1150" font-size="64" textLength="250" lengthAdjust="spacingAndGlyphs">BREVIX</text>
  </g>
</svg>
</body>
</html>
```